Bref créative
RON TALIVERO STATIONARY PACKAGE
Letterhead paper, Envelopes, Business Cards, Patient brochures, Flyer,Gift Certificate, T-Shirts
Professional
RON TALIVERO DDS
General & Cosmetic Dentistry
47-30 91 Street
Elmhurst, NY 11208
brightcuspdental@mailbox-example.com
www.brightcuspdental-example.com
I would like to present a very professional image for my company.
Smile!

```html
<!DOCTYPE html>
<html lang="en">
<head>
<meta charset="utf-8">
<title>Bright Cusp Dental – Flyer Colourways</title>
<link rel="stylesheet" href="https://fonts.googleapis.com/css2?family=Open+Sans:wght@400;600;800&display=swap">
<style>
  :root{
    --page:#e9e7e3;
    --paper:#ffffff;
    --ink:#3b3b3b;
    --muted:#666666;
    --gold:#d6a400;
    --charcoal:#1d1d1d;
    --green:#2f8a3e;
    --photo-warm-1:#f3e6d8;
    --photo-warm-2:#d9b79a;
    --photo-warm-3:#a9846a;
    --implant-1:#f1ece6;
    --implant-2:#c9b3a0;
    --family-1:#dfe8ef;
    --family-2:#b9c7d3;
  }
  *{box-sizing:border-box;margin:0;padding:0}
  html,body{width:1200px;height:605px;overflow:hidden}
  body{background:var(--page);font-family:"Open Sans",Arial,sans-serif;color:var(--ink)}

  .colourways{display:flex;justify-content:center;gap:15px;padding-top:72px}

  .flyer{--accent:var(--gold);--band:var(--gold);--band-text:#fff;
    width:355px;height:485px;background:var(--paper);
    box-shadow:0 2px 6px rgba(0,0,0,.18);display:flex;flex-direction:column;overflow:hidden}
  .flyer--gold{--accent:var(--gold);--band:var(--gold)}
  .flyer--charcoal{--accent:var(--gold);--band:var(--charcoal)}
  .flyer--green{--accent:var(--green);--band:var(--green)}

  .flyer__photo{height:140px;flex:none;position:relative;
    background:linear-gradient(160deg,var(--photo-warm-1) 0%,var(--photo-warm-2) 55%,var(--photo-warm-3) 100%)}
  .brand-mark{position:absolute;left:10px;top:10px;display:flex;align-items:center;gap:5px;
    background:rgba(255,255,255,.88);padding:4px 7px}
  .brand-mark__dot{width:10px;height:10px;border-radius:50%;background:var(--accent)}
  .brand-mark__name{font-size:9.5px;font-weight:600;color:var(--accent)}

  .flyer__title{font-size:21px;font-weight:800;color:var(--accent);
    letter-spacing:.3px;padding:9px 12px 6px;line-height:1;flex:none}

  .flyer__body{flex:1;min-height:0;display:grid;grid-template-columns:1fr 1fr;gap:10px;padding:0 12px 8px;overflow:hidden}
  .flyer__col{display:flex;flex-direction:column;gap:6px;min-height:0}
  .copy{font-size:6.6px;line-height:9.4px;color:var(--muted);text-align:justify}

  .feature{display:flex;gap:6px;align-items:flex-start;margin-top:auto}
  .feature__image{width:62px;height:72px;flex:none;
    background:linear-gradient(180deg,var(--implant-1),var(--implant-2))}
  .family-image{height:72px;flex:none;margin-top:auto;
    background:linear-gradient(135deg,var(--family-1),var(--family-2))}

  .flyer__footer{height:40px;flex:none;background:var(--band);color:var(--band-text);
    display:grid;grid-template-columns:1fr 1fr;gap:3px 8px;padding:6px 12px;align-content:center}
  .contact{display:flex;align-items:center;gap:4px;font-size:6.2px;line-height:1.2;white-space:nowrap;overflow:hidden}
  .contact svg{width:7px;height:7px;flex:none}
</style>
</head>
<body>
<main class="colourways">

  <article class="flyer flyer--gold">
    <div class="flyer__photo" role="img" aria-label="Photo of a smiling family of three lying together on a white bed">
      <div class="brand-mark"><span class="brand-mark__dot"></span><span class="brand-mark__name">Bright Cusp Dental</span></div>
    </div>
    <h1 class="flyer__title">BRIGHT CUSP DENTAL</h1>
    <div class="flyer__body">
      <div class="flyer__col">
        <p class="copy">Our gentle team offers general and cosmetic dentistry for the whole family. We take time to explain every step, answer your questions and build a care plan that fits your smile, your schedule and your budget. Regular checkups help catch small problems early, before they turn into pain or costly repairs. We clean, polish and examine each tooth with care, and we show you simple habits that keep teeth strong at home. Children are welcome from their very first tooth, and we make every visit calm, bright and fun.</p>
        <div class="feature">
          <div class="feature__image" role="img" aria-label="Illustration of a dental implant set in the gum beside natural teeth"></div>
          <p class="copy">Dental implants replace missing teeth with a strong, natural looking result that lasts for many years and feels just like your own.</p>
        </div>
      </div>
      <div class="flyer__col">
        <p class="copy">From routine cleanings and fillings to whitening, veneers and crowns, we use modern tools in a calm, friendly office. New patients are always welcome, and most insurance plans are accepted. Evening and Saturday visits are available for busy families. Our staff will gladly help with forms, payment plans and reminders so that every appointment runs on time.</p>
        <p class="copy">Book a visit today and bring the kids along. We look forward to meeting you.</p>
        <div class="family-image" role="img" aria-label="Photo of a mother and child smiling together"></div>
      </div>
    </div>
    <footer class="flyer__footer">
      <span class="contact"><svg viewBox="0 0 10 10"><path d="M5 0a3.5 3.5 0 0 0-3.5 3.5C1.5 6 5 10 5 10s3.5-4 3.5-6.5A3.5 3.5 0 0 0 5 0z" fill="currentColor"/></svg>12 Example Lane, Sampletown</span>
      <span class="contact"><svg viewBox="0 0 10 10"><path d="M2 0h2l1 2.5-1.3 1a6 6 0 0 0 2.8 2.8l1-1.3L10 6v2a2 2 0 0 1-2 2A8 8 0 0 1 0 2a2 2 0 0 1 2-2z" fill="currentColor"/></svg>(000) 555-0142</span>
      <span class="contact"><svg viewBox="0 0 10 10"><rect x=".5" y="2" width="9" height="6" fill="none" stroke="currentColor"/><path d="M.5 2 5 5.5 9.5 2" fill="none" stroke="currentColor"/></svg>brightcuspdental@mailbox-example.com</span>
      <span class="contact"><svg viewBox="0 0 10 10"><circle cx="5" cy="5" r="4.5" fill="none" stroke="currentColor"/><path d="M.5 5h9M5 .5c-2 2.5-2 6.5 0 9M5 .5c2 2.5 2 6.5 0 9" fill="none" stroke="currentColor"/></svg>www.brightcuspdental-example.com</span>
    </footer>
  </article>

  <article class="flyer flyer--charcoal">
    <div class="flyer__photo" role="img" aria-label="Photo of a smiling family of three lying together on a white bed">
      <div class="brand-mark"><span class="brand-mark__dot"></span><span class="brand-mark__name">Bright Cusp Dental</span></div>
    </div>
    <h1 class="flyer__title">BRIGHT CUSP DENTAL</h1>
    <div class="flyer__body">
      <div class="flyer__col">
        <p class="copy">Our gentle team offers general and cosmetic dentistry for the whole family. We take time to explain every step, answer your questions and build a care plan that fits your smile, your schedule and your budget. Regular checkups help catch small problems early, before they turn into pain or costly repairs. We clean, polish and examine each tooth with care, and we show you simple habits that keep teeth strong at home. Children are welcome from their very first tooth, and we make every visit calm, bright and fun.</p>
        <div class="feature">
          <div class="feature__image" role="img" aria-label="Illustration of a dental implant set in the gum beside natural teeth"></div>
          <p class="copy">Dental implants replace missing teeth with a strong, natural looking result that lasts for many years and feels just like your own.</p>
        </div>
      </div>
      <div class="flyer__col">
        <p class="copy">From routine cleanings and fillings to whitening, veneers and crowns, we use modern tools in a calm, friendly office. New patients are always welcome, and most insurance plans are accepted. Evening and Saturday visits are available for busy families. Our staff will gladly help with forms, payment plans and reminders so that every appointment runs on time.</p>
        <p class="copy">Book a visit today and bring the kids along. We look forward to meeting you.</p>
        <div class="family-image" role="img" aria-label="Photo of a mother and child smiling together"></div>
      </div>
    </div>
    <footer class="flyer__footer">
      <span class="contact"><svg viewBox="0 0 10 10"><path d="M5 0a3.5 3.5 0 0 0-3.5 3.5C1.5 6 5 10 5 10s3.5-4 3.5-6.5A3.5 3.5 0 0 0 5 0z" fill="currentColor"/></svg>12 Example Lane, Sampletown</span>
      <span class="contact"><svg viewBox="0 0 10 10"><path d="M2 0h2l1 2.5-1.3 1a6 6 0 0 0 2.8 2.8l1-1.3L10 6v2a2 2 0 0 1-2 2A8 8 0 0 1 0 2a2 2 0 0 1 2-2z" fill="currentColor"/></svg>(000) 555-0142</span>
      <span class="contact"><svg viewBox="0 0 10 10"><rect x=".5" y="2" width="9" height="6" fill="none" stroke="currentColor"/><path d="M.5 2 5 5.5 9.5 2" fill="none" stroke="currentColor"/></svg>brightcuspdental@mailbox-example.com</span>
      <span class="contact"><svg viewBox="0 0 10 10"><circle cx="5" cy="5" r="4.5" fill="none" stroke="currentColor"/><path d="M.5 5h9M5 .5c-2 2.5-2 6.5 0 9M5 .5c2 2.5 2 6.5 0 9" fill="none" stroke="currentColor"/></svg>www.brightcuspdental-example.com</span>
    </footer>
  </article>

  <article class="flyer flyer--green">
    <div class="flyer__photo" role="img" aria-label="Photo of a smiling family of three lying together on a white bed">
      <div class="brand-mark"><span class="brand-mark__dot"></span><span class="brand-mark__name">Bright Cusp Dental</span></div>
    </div>
    <h1 class="flyer__title">BRIGHT CUSP DENTAL</h1>
    <div class="flyer__body">
      <div class="flyer__col">
        <p class="copy">Our gentle team offers general and cosmetic dentistry for the whole family. We take time to explain every step, answer your questions and build a care plan that fits your smile, your schedule and your budget. Regular checkups help catch small problems early, before they turn into pain or costly repairs. We clean, polish and examine each tooth with care, and we show you simple habits that keep teeth strong at home. Children are welcome from their very first tooth, and we make every visit calm, bright and fun.</p>
        <div class="feature">
          <div class="feature__image" role="img" aria-label="Illustration of a dental implant set in the gum beside natural teeth"></div>
          <p class="copy">Dental implants replace missing teeth with a strong, natural looking result that lasts for many years and feels just like your own.</p>
        </div>
      </div>
      <div class="flyer__col">
        <p class="copy">From routine cleanings and fillings to whitening, veneers and crowns, we use modern tools in a calm, friendly office. New patients are always welcome, and most insurance plans are accepted. Evening and Saturday visits are available for busy families. Our staff will gladly help with forms, payment plans and reminders so that every appointment runs on time.</p>
        <p class="copy">Book a visit today and bring the kids along. We look forward to meeting you.</p>
        <div class="family-image" role="img" aria-label="Photo of a mother and child smiling together"></div>
      </div>
    </div>
    <footer class="flyer__footer">
      <span class="contact"><svg viewBox="0 0 10 10"><path d="M5 0a3.5 3.5 0 0 0-3.5 3.5C1.5 6 5 10 5 10s3.5-4 3.5-6.5A3.5 3.5 0 0 0 5 0z" fill="currentColor"/></svg>12 Example Lane, Sampletown</span>
      <span class="contact"><svg viewBox="0 0 10 10"><path d="M2 0h2l1 2.5-1.3 1a6 6 0 0 0 2.8 2.8l1-1.3L10 6v2a2 2 0 0 1-2 2A8 8 0 0 1 0 2a2 2 0 0 1 2-2z" fill="currentColor"/></svg>(000) 555-0142</span>
      <span class="contact"><svg viewBox="0 0 10 10"><rect x=".5" y="2" width="9" height="6" fill="none" stroke="currentColor"/><path d="M.5 2 5 5.5 9.5 2" fill="none" stroke="currentColor"/></svg>brightcuspdental@mailbox-example.com</span>
      <span class="contact"><svg viewBox="0 0 10 10"><circle cx="5" cy="5" r="4.5" fill="none" stroke="currentColor"/><path d="M.5 5h9M5 .5c-2 2.5-2 6.5 0 9M5 .5c2 2.5 2 6.5 0 9" fill="none" stroke="currentColor"/></svg>www.brightcuspdental-example.com</span>
    </footer>
  </article>

</main>
</body>
</html>
```